Professional Letterhead for electronic use

I would like to inquire, if you could help me to create a letterhead, mostly for electronic use. Preferably in word file, with fixed letterhead design (header and footer), but will allow to add text on the main body of the letter. I usually operate online and would like to be able to add text, convert it to PDF and send as an attachment.
Target Market(s)
High net worth clients.
Industry/Entity Type
Real Estate Agent
Font styles to use
Other font styles liked:
- Century Gothic
Requirements
Must have
- Company name, logo, full address, email address, landline number, website address, Brackwell Panel logo, TOVE logo, Company registration number
Nice to have
- Professional and elegant design

```html
<!DOCTYPE html>
<html lang="en">
<head>
<meta charset="utf-8">
<title>Corvane Estate Agents — Letterhead</title>
<link rel="stylesheet" href="https://fonts.googleapis.com/css2?family=Questrial&family=Open+Sans:wght@400;600&display=swap">
<style>
  :root {
    --plum: #4e1039;
    --berry: #7a1a47;
    --orange: #f26a2a;
    --orange-light: #f79a5c;
    --paper: #ffffff;
    --ink-white: #ffffff;
  }
  * { box-sizing: border-box; margin: 0; padding: 0; }
  html, body { width: 982px; height: 1200px; overflow: hidden; background: var(--paper); }
  .letterhead {
    position: relative;
    width: 982px;
    height: 1200px;
    background: var(--paper);
    font-family: "Open Sans", sans-serif;
  }
  .header-wave { position: absolute; top: 0; left: 0; width: 982px; height: 300px; }
  .brand {
    position: absolute; left: 50px; top: 55px;
    display: flex; align-items: center; gap: 30px;
  }
  .brand-mark {
    width: 96px; height: 96px; border-radius: 50%;
    background: var(--orange);
  }
  .brand-name {
    font-family: "Questrial", sans-serif;
    color: var(--ink-white);
    font-size: 36px; letter-spacing: 7px; line-height: 1;
  }
  .brand-tagline {
    font-family: "Questrial", sans-serif;
    color: var(--orange);
    font-size: 15px; letter-spacing: 4.5px; margin-top: 10px;
  }
  .contact {
    position: absolute; right: 57px; top: 52px;
    list-style: none; text-align: right;
  }
  .contact li {
    display: flex; justify-content: flex-end; align-items: center; gap: 10px;
    color: var(--orange); font-size: 19px; line-height: 26px;
  }
  .contact svg { width: 19px; height: 19px; flex: none; }
  .footer-bar {
    position: absolute; left: 34px; top: 1133px; width: 600px; height: 26px;
    background: var(--plum); color: var(--ink-white);
    display: flex; justify-content: space-between; align-items: center;
    padding: 0 10px 0 12px; font-size: 15px; letter-spacing: 0.3px;
  }
  .footer-bar .reg { font-size: 13px; }
  .badge-round {
    position: absolute; left: 648px; top: 1078px;
    width: 80px; height: 80px; border-radius: 50%;
    background: var(--berry);
  }
  .badge-panel {
    position: absolute; left: 744px; top: 1097px;
    width: 191px; height: 62px; border-radius: 3px;
    background: var(--berry);
  }
</style>
</head>
<body>
<main class="letterhead">
  <svg class="header-wave" viewBox="0 0 982 300" aria-hidden="true">
    <defs>
      <linearGradient id="ribbon" x1="0" y1="1" x2="1" y2="0">
        <stop offset="0" stop-color="#f9a36b"/>
        <stop offset="1" stop-color="#f05a22"/>
      </linearGradient>
    </defs>
    <path fill="url(#ribbon)" d="M585,0 H640 C560,45 490,135 420,205 C340,280 190,302 80,282 C45,275 18,263 0,252 V228 C20,240 50,252 90,260 C200,280 330,250 400,180 C460,120 520,40 600,0 Z"/>
    <path fill="var(--plum)" d="M0,0 H600 C520,40 460,120 400,180 C330,250 200,280 90,260 C50,252 20,240 0,228 Z"/>
  </svg>

  <div class="brand">
    <div class="brand-mark"></div>
    <div>
      <div class="brand-name">CORVANE</div>
      <div class="brand-tagline">ESTATE AGENTS</div>
    </div>
  </div>

  <ul class="contact">
    <li>020 7946 0381
      <svg viewBox="0 0 20 20"><circle cx="10" cy="10" r="8.5" fill="none" stroke="var(--plum)" stroke-width="1.6"/><path d="M7,5.5 l2,2 -1,1.2 c0.7,1.5 1.8,2.6 3.3,3.3 l1.2-1 2,2 -1.3,1.5 c-3.5-0.5-6.7-3.7-7.2-7.2z" fill="var(--plum)"/></svg>
    </li>
    <li>info@corvane.co.uk
      <svg viewBox="0 0 20 20"><path d="M2,8 L10,3 18,8 V17 H2 Z" fill="var(--plum)"/><path d="M2,8 L10,13 18,8" fill="none" stroke="#fff" stroke-width="1.4"/></svg>
    </li>
    <li>www.corvane.co.uk
      <svg viewBox="0 0 20 20" fill="none" stroke="var(--plum)" stroke-width="1.5"><circle cx="10" cy="10" r="8.5"/><ellipse cx="10" cy="10" rx="4" ry="8.5"/><path d="M1.5,10 H18.5 M3,5.5 H17 M3,14.5 H17"/></svg>
    </li>
  </ul>

  <footer>
    <div class="footer-bar">
      <span class="address">Corvane Ltd, 412A Harrowden Road, London NW9 4LT</span>
      <span class="reg">Reg No: 04718263</span>
    </div>
    <div class="badge-round" role="img" aria-label="TOVE membership badge"></div>
    <div class="badge-panel" role="img" aria-label="Brackwell Panel membership badge"></div>
  </footer>
</main>
</body>
</html>
```